Real Estate Development Company Stationary

We need our company, business card, letterhead, pocket folder and envelope designed.

We are a new real estate development company. We focus on data centre, commercial and real estate development.

Please see attached for our logo. Since it's a new logo, you still can make minor adjust if you like it makes senses

The client has sent me a business card he really likes. Please see file 3.

Target Market(s)

Real Estate Investors
Large corporations
Home buyers

Industry/Entity Type

Real Estate

```html
<!DOCTYPE html>
<html lang="en">
<head>
<meta charset="utf-8">
<title>Envelope Template</title>
<link rel="stylesheet" href="https://fonts.googleapis.com/css2?family=Jost:wght@400;500&display=swap">
<style>
  :root {
    --slate: #2e3e46;
    --paper: #ffffff;
    --fold: #b4b4b4;
    --brand-blue: #00417f;
    --brand-green: #74c044;
    --mid-green: #4a9059;
    --deep-teal: #2b6b6e;
    --ink: #111111;
  }
  * { margin: 0; padding: 0; box-sizing: border-box; }
  html, body { width: 1200px; height: 744px; overflow: hidden; }
  body {
    background: var(--slate);
    font-family: "Jost", "Futura", sans-serif;
    position: relative;
  }
  .sheet-title {
    position: absolute;
    left: 30px; top: 24px;
    color: var(--paper);
    font-size: 37px;
    font-weight: 400;
    letter-spacing: 0.2px;
  }
  .envelope-die { position: absolute; left: 0; top: 0; }
  .return-address {
    position: absolute;
    left: 273px; top: 607px;
    font-size: 11.5px;
    color: var(--ink);
  }
  .brand-lockup {
    position: absolute;
    left: 812px; top: 548px;
    display: flex; align-items: center; gap: 12px;
  }
  .brand-dot {
    width: 40px; height: 40px;
    border-radius: 50%;
    background: var(--brand-green);
  }
  .brand-name {
    color: var(--brand-blue);
    font-size: 22px;
    font-weight: 500;
    line-height: 1;
  }
  .footer-web {
    position: absolute;
    left: 273px; top: 639px;
    color: var(--paper);
    font-size: 16px;
    letter-spacing: 0.3px;
  }
  .footer-contact {
    position: absolute;
    right: 154px; top: 643px;
    color: var(--paper);
    font-size: 12.5px;
    word-spacing: 1px;
  }
  .footer-contact b { font-weight: 500; }
  .footer-contact .gap { display: inline-block; width: 10px; }
</style>
</head>
<body>
  <h1 class="sheet-title">Envelope Template</h1>

  <svg class="envelope-die" width="1200" height="744" viewBox="0 0 1200 744" aria-hidden="true">
    <path fill="var(--paper)" d="M112,232 L148,122 Q156,100 180,100 L1034,100 Q1058,100 1066,122 L1102,232 L1140,268 Q1168,284 1168,302 L1168,638 Q1168,660 1140,678 L1102,701 L1090,720 L1088,744 L125,744 L124,720 L112,701 L74,678 Q45,660 45,638 L45,302 Q45,284 74,268 Z"/>
    <rect class="footer-band" x="112" y="632" width="990" height="69" fill="var(--brand-blue)"/>
    <rect x="112" y="632" width="86" height="69" fill="var(--brand-green)"/>
    <rect x="198" y="632" width="46" height="69" fill="var(--mid-green)"/>
    <rect x="244" y="632" width="14" height="69" fill="var(--deep-teal)"/>
    <rect class="fold-lines" x="112.5" y="232.5" width="989" height="468" fill="none" stroke="var(--fold)" stroke-width="1.2" stroke-dasharray="6 4"/>
  </svg>

  <p class="return-address">Address here, City, State, Zip Code</p>

  <div class="brand-lockup">
    <span class="brand-dot"></span>
    <span class="brand-name">Novar Development Inc.</span>
  </div>

  <p class="footer-web">www.novardevelopment.ca</p>
  <p class="footer-contact"><b>T</b> 416-555-0147<span class="gap"></span><b>E</b> info@novardevelopment.ca</p>
</body>
</html>
```